電子書籍の表紙を作成お願い致します。

50歳以上の更年期女性が対象のダイエット本です。
更年期をむかえてから、ソウルメロディダイエットで7キロ痩せることに成功した体験が書かれています。

たくさんあるダイエット本に埋もれないような、
ダイエットという言葉に反応する、美意識の高い更年期女性の目につく、明るく楽し気なデザインを期待しています。

その他、何か不明な点等ございましたら、お気軽におtぴ合わせください。

宜しくお願い致します。

著者顔写真と原稿を追記します。
参考にしてください。
著者の肩書は、
ダイエットアドバイザー フィットネスインストラクター
とよろしくお願いいたします。
募集締め切りがいよいよ16時間をきりました。
すでに、いくつかの素敵なデザインをいただいていますが、
最後の逆転大ホームランを狙っている、あなたの応募を心よりお待ちしています。

選んだ理由としては、
①美意識高い女性が好むピンクがメインのデザイン
②ソウルメロディダイエットもタイトルが一番見やすい
③ビフォーアフターのイラストが可愛い
などです。

この度は、たくさんの素敵なデザインを提案いただき、本当にありがとうございました。
初めての電子書籍で大変でしたが、デザイナーの皆さんのおかげで、毎日ワクワクして、
この表紙選定が一番楽しい作業になりました。

今回残念ながら、次点になった2点もとても評判が良いものでした。
そのほかのデザインも、とても個性的で素敵でした。
本当にありがとうございました。

次回お世話になる際には、またよろしくお願いいたします。

```html
<!DOCTYPE html>
<html lang="ja">
<head>
<meta charset="UTF-8">
<title>50才から脳で痩せる</title>
<link rel="stylesheet" href="https://fonts.googleapis.com/css2?family=Noto+Serif+JP:wght@500;700;900&family=Noto+Sans+JP:wght@500;700;900&display=swap">
<style>
  :root {
    --paper: #f4f1df;
    --ink: #262322;
    --pink: #c6477a;
    --band: #c4507f;
    --lilac: #dcc0d4;
    --white: #ffffff;
  }
  * { margin: 0; padding: 0; box-sizing: border-box; }
  html, body { width: 750px; height: 1200px; overflow: hidden; }
  body { background: var(--paper); }
  .cover {
    position: relative;
    width: 750px;
    height: 1200px;
    background: var(--paper);
    color: var(--ink);
    font-family: "Noto Serif JP", serif;
    overflow: hidden;
  }
  .brain-art {
    position: absolute;
    left: 225px;
    top: 215px;
    width: 450px;
    height: 445px;
    border-radius: 48% 48% 42% 42%;
    background: radial-gradient(ellipse at center, rgba(220,192,212,0.15) 0%, rgba(220,192,212,0.45) 70%, rgba(220,192,212,0.1) 100%);
  }
  .age-bubble {
    position: absolute;
    left: 118px;
    top: 118px;
    width: 160px;
    height: 100px;
  }
  .age-bubble span {
    position: absolute;
    left: 0; top: 12px;
    width: 152px;
    text-align: center;
    font-family: "Noto Sans JP", sans-serif;
    font-weight: 700;
    font-size: 28px;
    color: var(--pink);
    letter-spacing: 1px;
  }
  .title-char {
    position: absolute;
    font-weight: 900;
    line-height: 1;
    color: var(--ink);
    transform: translateX(-50%);
    left: 450px;
  }
  .t-nou { top: 132px; font-size: 158px; }
  .t-de  { top: 300px; font-size: 82px; }
  .t-ya  { top: 395px; font-size: 140px; }
  .t-se  { top: 535px; font-size: 112px; }
  .t-ru  { top: 630px; font-size: 118px; }
  .author {
    position: absolute;
    left: 160px;
    top: 500px;
    writing-mode: vertical-rl;
    font-family: "Noto Sans JP", sans-serif;
  }
  .author .label { font-size: 18px; font-weight: 500; margin-left: 0; display: block; }
  .author-name {
    position: absolute;
    left: 158px;
    top: 548px;
    writing-mode: vertical-rl;
    font-family: "Noto Sans JP", sans-serif;
    font-weight: 500;
    font-size: 28px;
    letter-spacing: 4px;
  }
  .lead {
    position: absolute;
    right: 40px;
    top: 750px;
    text-align: right;
    font-family: "Noto Sans JP", sans-serif;
    font-weight: 700;
    font-size: 24px;
    line-height: 45px;
  }
  .lead .key {
    display: inline-block;
    border: 2.5px solid var(--pink);
    padding: 0 6px;
    line-height: 34px;
    margin-right: 4px;
  }
  .band {
    position: absolute;
    left: 0;
    top: 930px;
    width: 750px;
    height: 270px;
    background: var(--band);
    color: var(--white);
    text-align: center;
  }
  .band-question {
    position: absolute;
    left: 50%;
    top: 68px;
    transform: translateX(-50%);
    white-space: nowrap;
    font-family: "Noto Sans JP", sans-serif;
    font-weight: 500;
    font-size: 26px;
    letter-spacing: 2px;
    border: 2px solid var(--white);
    border-radius: 40px;
    padding: 6px 34px;
  }
  .band-claim {
    position: absolute;
    left: 0;
    width: 100%;
    top: 148px;
    font-weight: 700;
    font-size: 40px;
    letter-spacing: 2px;
  }
</style>
</head>
<body>
  <main class="cover">
    <div class="brain-art" role="img" aria-label="脳の線画イラスト"></div>

    <div class="age-bubble">
      <svg width="160" height="100" viewBox="0 0 160 100">
        <path d="M30 6 H122 A24 24 0 0 1 146 30 V44 A24 24 0 0 1 122 68 H112 L120 92 L96 68 H30 A24 24 0 0 1 6 44 V30 A24 24 0 0 1 30 6 Z"
              fill="none" stroke="#c6477a" stroke-width="3"/>
      </svg>
      <span>50才から</span>
    </div>

    <h1 class="book-title">
      <span class="title-char t-nou">脳</span>
      <span class="title-char t-de">で</span>
      <span class="title-char t-ya">痩</span>
      <span class="title-char t-se">せ</span>
      <span class="title-char t-ru">る</span>
    </h1>

    <div class="author"><span class="label">著</span></div>
    <div class="author-name">氏名氏名</div>

    <p class="lead">
      <span class="key">更年期</span>を迎えてから<br>
      <span class="key">ソウルメロディダイエット</span>で<br>
      <span class="key">7キロ</span>痩せることに成功！？
    </p>

    <section class="band">
      <p class="band-question">キレイになること、諦めていませんか？</p>
      <p class="band-claim">50歳でジブン史上最高に</p>
    </section>
  </main>
</body>
</html>
```